Holistic Psychologist needs contemporary business card

I am a psychologist working with adult clients face to face and online. The card needs to work for clients and also referring doctors and medical professionals. It needs to look warm, safe and trustable for clients, but clean and professional enough for doctors. Sometimes I also work in a corporate context.

I am holistic in my approach (mind-body-spirit) so anything conveying connection or integration or wholeness would be good. But again, clean and contemporary please. It can have a little bit of personality.
New logo uploaded.

Probably warm tones and plenty white space to write on one side.

My web pages:
http://lmtherapy.com.au
https://www.facebook.com/MarcellaWhitfordTherapy?ref=hl
Updates

Hi Designers .. I have decided I do need a new logo before finalising a design for the business cards.  I hope to have this available in 4 days from now.

Kindly,

Marcella

New logo now posted, same brief.  Balance of masculine and feminine elements, plenty of white space on one side please.

Keen to see some card designs, thank-you.

Target Market(s)

Audience 1 - Males and females aged 25 years + seeking counselling or coaching. Audience 2 - doctors and health professionals who refer clients.

Industry/Entity Type

Medical

Contact Information for Business Card

Logo

Marcella Whitford
Registered Psychologist

M: 0491 508 243
www.lmtherapy.com.au
marcella@lmtherapy.com.au
Little blue Facebook icon, with "marcella whitford therapy" printed near it.

Font styles to use
Sans Serif

Requirements
Nice to have
• You might want to play with the words "essential you"
Should not have
• Nothing cutesy or too literal

```html
<!DOCTYPE html>
<html lang="en">
<head>
<meta charset="utf-8">
<title>Marcella Whitford Therapy – Business Card</title>
<link href="https://fonts.googleapis.com/css2?family=Ubuntu:wght@300;400&display=swap" rel="stylesheet">
<style>
  :root {
    --canvas: #ecebe8;
    --card: #ffffff;
    --red: #e31e26;
    --ink: #1a1a1a;
    --grey: #5b5b5b;
    --rule: #9a9a9a;
    --social: #3b5998;
  }
  * { box-sizing: border-box; margin: 0; padding: 0; }
  html, body { width: 1200px; height: 1024px; overflow: hidden; }
  body {
    background: var(--canvas);
    font-family: "Ubuntu", sans-serif;
    position: relative;
  }
  .card {
    position: absolute;
    left: 250px;
    width: 700px;
    height: 400px;
    background: var(--card);
    box-shadow: 0 6px 18px rgba(0,0,0,.12);
    overflow: hidden;
  }
  .card--front { top: 90px; }
  .card--back { top: 540px; }

  /* Brand lockup */
  .brand {
    display: flex;
    align-items: center;
    gap: 14px;
  }
  .brand__dot {
    width: 34px; height: 34px;
    border-radius: 50%;
    background: var(--red);
    flex: none;
  }
  .brand__name {
    color: var(--red);
    font-weight: 300;
    font-size: 36px;
    letter-spacing: .5px;
    white-space: nowrap;
  }

  /* Front */
  .card--front .brand { position: absolute; left: 52px; top: 64px; }
  .person { position: absolute; left: 118px; top: 156px; }
  .person__name { color: var(--red); font-size: 21px; font-weight: 400; }
  .person__role { color: var(--grey); font-size: 21px; font-weight: 300; margin-top: 2px; }
  .contacts { position: absolute; left: 118px; top: 232px; list-style: none; }
  .contacts li {
    display: flex; align-items: center; gap: 8px;
    color: var(--grey); font-size: 19px; font-weight: 300; line-height: 27px;
  }
  .contacts svg { width: 15px; height: 15px; flex: none; }
  .band-red {
    position: absolute; left: 0; bottom: 0;
    width: 100%; height: 26px;
    background: var(--red);
  }
  .tab-web {
    position: absolute; right: 0; bottom: 0;
    width: 290px; height: 52px;
    background: var(--ink);
    border-top-left-radius: 26px;
    display: flex; align-items: center; justify-content: center;
    color: #ffffff; font-size: 17px; font-weight: 300; letter-spacing: .5px;
  }

  /* Back */
  .card--back .brand { position: absolute; right: 48px; top: 52px; }
  .card--back .brand__name { font-size: 30px; }
  .appointment { position: absolute; left: 44px; top: 140px; width: 612px; list-style: none; }
  .appointment li {
    display: flex; align-items: flex-end; gap: 10px;
    height: 46px;
    color: var(--grey); font-size: 17px; font-weight: 300; letter-spacing: 1px;
  }
  .appointment .label { width: 58px; }
  .appointment .line { flex: 1; border-bottom: 1px solid var(--rule); margin-bottom: 5px; }
  .back-web {
    position: absolute; left: 44px; bottom: 34px;
    color: var(--red); font-size: 16px; font-weight: 300;
  }
</style>
</head>
<body>

<section class="card card--front" aria-label="Business card front">
  <div class="brand">
    <span class="brand__dot"></span>
    <span class="brand__name">Marcella Whitford Therapy</span>
  </div>

  <div class="person">
    <p class="person__name">Marcella Whitford</p>
    <p class="person__role">Registered Psychologist</p>
  </div>

  <ul class="contacts">
    <li>
      <svg viewBox="0 0 16 16" aria-hidden="true"><rect x="1" y="1" width="14" height="14" rx="2" fill="none" stroke="#e31e26" stroke-width="2"/><rect x="5.5" y="3.5" width="5" height="9" rx="1" fill="#e31e26"/></svg>
      0491 508 243
    </li>
    <li>
      <svg viewBox="0 0 16 16" aria-hidden="true"><rect x="0" y="0" width="16" height="16" rx="2" fill="#e31e26"/><path d="M3 5h10v7H3z M3 5l5 4 5-4" fill="none" stroke="#fff" stroke-width="1.3"/></svg>
      marcella@lmtherapy.com.au
    </li>
    <li>
      <svg viewBox="0 0 16 16" aria-hidden="true"><rect x="0" y="0" width="16" height="16" rx="2" fill="#3b5998"/></svg>
      marcella whitford therapy
    </li>
  </ul>

  <div class="band-red"></div>
  <div class="tab-web">www.lmtherapy.com.au</div>
</section>

<section class="card card--back" aria-label="Business card back">
  <div class="brand">
    <span class="brand__dot"></span>
    <span class="brand__name">Marcella Whitford Therapy</span>
  </div>

  <ul class="appointment">
    <li><span class="label">FOR:</span><span class="line"></span></li>
    <li><span class="label">DAY:</span><span class="line"></span></li>
    <li><span class="label">DATE:</span><span class="line"></span></li>
    <li><span class="label">TIME:</span><span class="line"></span></li>
  </ul>

  <p class="back-web">www.lmtherapy.com.au</p>
</section>

</body>
</html>
```